Body therapist needs a business card

I need a card for my business which is teaching trainings in body therapy, the company is called Wexcombe Educational Group. I teach to massage therapists around Australia, South East Asia and the USA. I am attaching my logo which will guide you as to what colours I would like to have you consider. Please consult my website to find out more about what I do. www.corvantela.com.au

My name is Daniel Wexcombe. My phone number is (03) 9417 2608 or 0461753208. email is info@corvantela.com.au

```html
<!DOCTYPE html>
<html lang="en">
<head>
<meta charset="utf-8">
<title>Wexcombe Educational Group – Business Card</title>
<link rel="stylesheet" href="https://fonts.googleapis.com/css2?family=Fira+Sans:wght@300;400&display=swap">
<style>
  :root {
    --stage-light: #ffffff;
    --stage-dark: #5a5b5d;
    --card-white: #ffffff;
    --earth-brown: #6e3316;
    --logo-brown: #8e4a22;
    --lime: #cbdc2c;
    --berry-red: #b80c0c;
    --name-cream: #f3e6da;
    --contact-lime: #c9d52e;
    --wordmark: #8a5a3e;
  }
  * { box-sizing: border-box; margin: 0; padding: 0; }
  html, body {
    width: 1200px; height: 1200px; overflow: hidden;
    font-family: "Fira Sans", Arial, sans-serif;
  }
  .canvas { position: relative; width: 1200px; height: 1200px; }
  .stage-top { position: absolute; left: 0; top: 0; width: 1200px; height: 600px; background: var(--stage-light); }
  .stage-bottom { position: absolute; left: 0; top: 600px; width: 1200px; height: 600px; background: var(--stage-dark); }

  .card {
    position: absolute; left: 356px; width: 474px; height: 270px; overflow: hidden;
    box-shadow: 0 14px 18px -8px rgba(0,0,0,0.45);
  }
  .card-front { top: 152px; background: var(--card-white); outline: 1px solid #222; }
  .card-back { top: 747px; background: var(--earth-brown); }
  .card-shapes { position: absolute; inset: 0; width: 474px; height: 270px; }

  .brand { position: absolute; left: 19px; top: 99px; display: flex; align-items: center; gap: 11px; }
  .brand-dot { width: 64px; height: 64px; border-radius: 50%; background: var(--logo-brown); }
  .brand-name { color: var(--wordmark); font-weight: 300; line-height: 1; }
  .brand-name .main { display: block; font-size: 22px; }
  .brand-name .sub { display: block; font-size: 9.5px; margin-top: 4px; }

  .holder {
    position: absolute; left: 20px; top: 114px;
    color: var(--name-cream); font-weight: 300; font-size: 22px; letter-spacing: 0.1px;
  }
  .contacts {
    position: absolute; left: 20px; top: 146px;
    display: flex; align-items: center; gap: 5px;
    color: var(--contact-lime); font-weight: 300; font-size: 9px; white-space: nowrap;
  }
  .contact-item { display: flex; align-items: center; gap: 2px; }
  .contact-item svg { width: 11px; height: 11px; flex: none; }
</style>
</head>
<body>
<div class="canvas">
  <div class="stage-top"></div>
  <div class="stage-bottom"></div>

  <section class="card card-front" aria-label="Card front">
    <svg class="card-shapes" viewBox="0 0 474 270" aria-hidden="true">
      <circle cx="419" cy="-34" r="169" fill="var(--earth-brown)"/>
      <circle cx="419" cy="-34" r="146" fill="var(--lime)"/>
      <circle cx="69" cy="323" r="95" fill="var(--earth-brown)"/>
      <circle cx="69" cy="323" r="69" fill="var(--berry-red)"/>
    </svg>
    <div class="brand">
      <div class="brand-dot"></div>
      <div class="brand-name">
        <span class="main">Wexcombe</span>
        <span class="sub">Educational Group</span>
      </div>
    </div>
  </section>

  <section class="card card-back" aria-label="Card back">
    <svg class="card-shapes" viewBox="0 0 474 270" aria-hidden="true">
      <circle cx="419" cy="-34" r="169" fill="var(--card-white)"/>
      <circle cx="419" cy="-34" r="146" fill="var(--earth-brown)"/>
      <circle cx="69" cy="323" r="95" fill="var(--card-white)"/>
      <circle cx="69" cy="323" r="70" fill="var(--earth-brown)"/>
    </svg>
    <h1 class="holder">Daniel Wexcombe</h1>
    <div class="contacts">
      <span class="contact-item">
        <svg viewBox="0 0 12 12"><path d="M3 1 L5 3.5 L4 4.8 Q5 7 7.2 8 L8.5 7 L11 9 L9.8 11 Q4.5 11 1 3.5 Z" fill="var(--contact-lime)"/></svg>
        (03) 9417 2608, 0461753208
      </span>
      <span class="contact-item">
        <svg viewBox="0 0 12 12"><rect x="0.5" y="2.5" width="11" height="7" fill="var(--contact-lime)"/><path d="M0.5 2.5 L6 6.5 L11.5 2.5" stroke="var(--earth-brown)" stroke-width="0.8" fill="none"/></svg>
        info@corvantela.com.au
      </span>
      <span class="contact-item">
        <svg viewBox="0 0 12 12"><circle cx="6" cy="6" r="5.2" fill="var(--contact-lime)"/><g stroke="var(--earth-brown)" stroke-width="0.6" fill="none"><ellipse cx="6" cy="6" rx="2.2" ry="5.2"/><line x1="0.8" y1="6" x2="11.2" y2="6"/><line x1="1.6" y1="3.5" x2="10.4" y2="3.5"/><line x1="1.6" y1="8.5" x2="10.4" y2="8.5"/></g></svg>
        www.corvantela.com.au
      </span>
    </div>
  </section>
</div>
</body>
</html>
```